Simple but impressive brochure for Consulting Company

We need a single page (back and front) brochure to introduce our company to prospective clients. We are open to different formats, but think that a trifold or double fold may work best. (fold up style brochure or a flyer with front & back).

It should be easy to print as we will need to print it as soon as possible. 8 1/2 x 11 based format is probably best, but again, we are open to suggestions.

About the Company:

We are a consulting company comprised of US Navy fighter pilots (SKYLANCE), US Navy SEALS, and business executives, that use our knowledge and experience in high risk / high performance environments to benefit our business clients. Most of our clients are in the oil and mining sector.

We deal with drilling companies and their crews and management. We do lectures and provide on-site training and coaching.

Enclosed in the "file" section are various one page handouts with information that describes what we do and how we currently project our image to our clients.

Our website is http://www.veltmorix.example

We have photographs of worksites, fighter jets, etc. available for creative use, if the quality is deemed acceptable by you, the designer, to use. We are not opposed to stock photos if those would be preferable.

We are working on a fairly tight schedule as we have an event on 4 February 2013. So we need the design done and enough time to have the final version printed. We set this project at 5 days, but can extend it a bit as needed.

We are looking for a design that is solid, professional and gives an indication of our background in high risk environments, but does not over emphasis our military experience.

Oil field related imagery would be a nice addition. In our business, we emphasis and sell the concept of SAFE and RELIABLE operations, done by people with vast experience in the field.

We take our experience in the field and aircraft carrier operations and pass those lessons to the oil field and mining operations. (primarily oil field)

In case you need to know: we have a few different versions of our LOGO in the attached files. It consists of an orb and the word KESTRAN in "Good Times" font, slightly flattened and stretched. (you can see the logo files). We also use a Kestran AXIS(tm) logo for a specific set of programs we offer.

Note: We have more files to upload, but currently it is maxed at 5 files. They will be uploaded if more are allowed or put in a Filevat.

Thank you all for your participation.  I'm sorry I could only pick one design, as so many of you are very talented and made the choice difficult.

Target Market(s)

Our buyers are managers and executives of Meridel 400 companies. Primarily male, educated, many with engineering backgrounds.

Industry/Entity Type

Training

Requirements
Must have
• Our primary desire is to convey a sense of action and professionalism to our prospective clients. I'm not sure if we have anything compulsory required with the exception of our logo.

If there is room and it makes sense, we can include the "Service Disabled Veteran" logo. (in file section)

Nice to have
• We would like an ongoing relationship with our selected designer. We will have updated brochures and web graphics in the near future.

```html
<!DOCTYPE html>
<html lang="en">
<head>
<meta charset="utf-8">
<title>Kestran Trifold Brochure</title>
<link rel="stylesheet" href="https://fonts.googleapis.com/css2?family=Montserrat:wght@400;500;700&display=swap">
<style>
  :root {
    --backdrop: #2b2b2d;
    --paper: #ffffff;
    --ink: #3a3a3a;
    --ink-soft: #6b6b6b;
    --grey-light: #f1f1f1;
    --grey-mid: #d6d6d6;
    --grey-band: #a9a9a9;
    --sky-top: #4f77a8;
    --sky-low: #8fb0cf;
    --sea: #2d4f80;
    --badge: #2a4a9a;
  }
  * { box-sizing: border-box; margin: 0; padding: 0; }
  html, body { width: 1200px; height: 865px; overflow: hidden; }
  body {
    background: var(--backdrop);
    font-family: "Montserrat", Arial, sans-serif;
    color: var(--ink);
    position: relative;
  }
  .brochure {
    position: absolute;
    left: 30px; top: 18px;
    width: 1140px; height: 829px;
    background: var(--paper);
    display: flex;
  }
  .panel { position: relative; width: 380px; height: 100%; }
  .panel + .panel { border-left: 1px solid #e4e4e4; }

  /* Inside panel */
  .panel--inside { padding: 46px 40px 40px 44px; text-align: right; }
  .section { margin-bottom: 26px; }
  .section__title {
    font-size: 13px; font-weight: 700; color: var(--ink);
    margin-bottom: 8px;
  }
  .section__text {
    font-size: 10.5px; line-height: 1.6; color: var(--ink-soft);
  }

  /* Cover spread (middle + right) */
  .cover {
    position: absolute; left: 380px; top: 0;
    width: 760px; height: 100%;
  }
  .cover svg { position: absolute; inset: 0; }
  .intro {
    position: absolute; left: 430px; top: 112px; width: 280px;
    font-size: 12px; line-height: 1.55; color: var(--ink); text-align: center;
  }
  .badge {
    position: absolute; left: 540px; top: 34px;
    width: 60px; height: 60px; border-radius: 50%;
    background: var(--paper); border: 6px solid var(--badge);
  }
  .brand {
    position: absolute; left: 800px; top: 150px; width: 330px;
    text-align: center;
    font-size: 34px; font-weight: 500; color: var(--ink);
  }
</style>
</head>
<body>
  <main class="brochure">
    <section class="panel panel--inside">
      <div class="section">
        <h2 class="section__title">Kestran's Mission</h2>
        <p class="section__text">Operational, Safety &amp; Commercial Excellence in Complex Environments</p>
      </div>
      <div class="section">
        <h2 class="section__title">Foundation of Excellence</h2>
        <p class="section__text">The Foundation of Excellence is built on leadership, culture, communication, high reliability and safety. It sets expectations, reinforces disciplines and aligns every level of the organization around the mission.</p>
      </div>
      <div class="section">
        <h2 class="section__title">Engine of Excellence</h2>
        <p class="section__text">Kestran instills the disciplines of Planning, Briefing, Execution, and the After-Action Review (AAR) that drive levels of excellence and continuous improvement. The Engine of Excellence yields predictable, repeatable results. Our methodology creates accountability and a disciplined culture for realizing your organization's vision.</p>
      </div>
      <div class="section">
        <h2 class="section__title">Human Performance</h2>
        <p class="section__text">The human element is the most important factor for success in complex high-risk organizations. Kestran training focuses on the strengths and weaknesses of the human component. Our solutions are built to optimize leadership, communications, teamwork, situational awareness, and more.</p>
      </div>
      <div class="section">
        <h2 class="section__title">Kestran AXIS&trade;</h2>
        <p class="section__text">The drive toward zero incidents is the hallmark of high performing complex high-risk organizations. Our Kestran AXIS&trade; family of programs builds the skill sets required for organizations and individuals to embark on a true journey of excellence.</p>
      </div>
    </section>
    <section class="panel"></section>
    <section class="panel"></section>

    <div class="cover">
      <svg width="760" height="829" viewBox="0 0 760 829">
        <defs>
          <linearGradient id="sky" x1="0" y1="0" x2="0" y2="1">
            <stop offset="0" stop-color="var(--sky-top)"/>
            <stop offset="0.6" stop-color="var(--sky-low)"/>
            <stop offset="0.62" stop-color="var(--sea)"/>
            <stop offset="1" stop-color="#23436f"/>
          </linearGradient>
          <linearGradient id="greyTop" x1="0" y1="0" x2="0" y2="1">
            <stop offset="0" stop-color="var(--grey-light)"/>
            <stop offset="1" stop-color="var(--grey-mid)"/>
          </linearGradient>
        </defs>
        <rect class="photo" x="0" y="260" width="760" height="569" fill="url(#sky)" role="img" aria-label="Offshore oil drilling platform with cranes standing in calm blue sea under a clear sky"/>
        <path class="band band--dark" d="M0,300 C120,380 300,380 380,340 C500,380 640,440 760,470 L760,0 L0,0 Z" fill="var(--grey-band)"/>
        <path class="band band--white" d="M0,280 C120,360 300,360 380,318 C500,360 640,418 760,446 L760,0 L0,0 Z" fill="#fafafa"/>
        <path class="band band--grey" d="M0,265 C120,345 300,345 380,300 C500,342 640,398 760,425 L760,0 L0,0 Z" fill="url(#greyTop)"/>
      </svg>
    </div>

    <div class="badge" role="img" aria-label="Certification badge"></div>
    <p class="intro">Kestran is a high performance training and consulting company with high performance people. Kestran's team consists of Fighter Pilots, Navy SEALS, Special Forces, Astronauts, and veteran industry &amp; corporate leaders. We leverage the credibility, experience, expertise, and ingenuity of our team to develop solutions for our clients.</p>

    <p class="brand">Kestran</p>
  </main>
</body>
</html>
```